New website for our Escape Room

We are wanting to create a new website for our website. We have 2 different locations that guests will choose their location on the home page. Then we have 5 different escape room experiences. We like clean and fresh but fun. Our logo is black white and red. We like a modern feel that is simple to navigate. I love movement on the page. You can see our current site at lockwickpuzzlehall.example
We like fresh and modern. It needs to include much of the same information as out current site but we won't like the look of our site.

Target Market(s)

amusement, escape rooms.

Industry/Entity Type

escape room

Number of Pages Required

4 page

Requirements
Must have
• info on all 4 escape rooms, option to choose between Pine Hollow and Riverton locations.

```html
<!DOCTYPE html>
<html lang="en">
<head>
<meta charset="utf-8">
<title>Lockwick Puzzle Hall – Escape Rooms</title>
<link rel="stylesheet" href="https://fonts.googleapis.com/css2?family=Oswald:wght@400;500;600;700&family=Open+Sans:wght@400;600;700&display=swap">
<style>
:root{
  --red:#e3000f;
  --red-dark:#8a0008;
  --black:#0b0b0b;
  --panel:#141414;
  --card:#1d1d1d;
  --white:#ffffff;
  --grey:#bdbdbd;
  --head:'Oswald', sans-serif;
  --body:'Open Sans', sans-serif;
}
*{box-sizing:border-box;margin:0;padding:0}
html,body{width:1200px;height:3556px;overflow:hidden;background:var(--black);color:var(--white);font-family:var(--body)}
.page{position:relative;width:1200px;height:3556px;overflow:hidden}
.section-title{font-family:var(--head);font-weight:600;font-size:40px;text-align:center;letter-spacing:.5px;text-transform:uppercase}
.title-bar{width:40px;height:5px;background:var(--red);margin:14px auto 0}
.btn{display:inline-block;font-family:var(--head);font-weight:500;font-size:16px;text-transform:uppercase;padding:12px 34px;border-radius:24px;background:var(--red);color:var(--white);text-decoration:none}
.btn-light{background:var(--white);color:var(--red)}
/* Header */
.site-nav{position:absolute;top:0;left:0;width:1200px;height:76px;display:flex;align-items:center;padding:0 130px;z-index:3}
.brand{display:flex;align-items:center;gap:10px;font-family:var(--head);font-weight:600;font-size:30px;color:var(--white)}
.brand-mark{width:12px;height:12px;background:var(--red)}
.nav-links{margin-left:auto;display:flex;gap:30px;list-style:none}
.nav-links a{color:var(--white);text-decoration:none;font-family:var(--head);font-size:14px;font-weight:500}
.nav-links .active a{color:var(--red)}
/* Hero */
.hero{position:absolute;top:0;left:0;width:1200px;height:580px}
.hero-bg{position:absolute;inset:0;background:radial-gradient(ellipse at 50% 35%,#9a1a1f 0%,#5a0a0e 45%,#1a0204 85%)}
.hero-content{position:absolute;top:120px;width:100%;text-align:center}
.hero-logo{display:inline-flex;align-items:center;gap:18px;font-family:var(--head);font-weight:600;font-size:118px;line-height:1;letter-spacing:2px}
.hero-logo .brand-mark{width:28px;height:28px}
.hero-tag{font-family:var(--head);font-weight:500;font-size:30px;color:var(--red);margin-top:18px;letter-spacing:1px}
.hero-actions{margin-top:24px;display:flex;gap:24px;justify-content:center}
.hero-actions .btn{width:180px}
.hero-slant{position:absolute;left:0;top:470px}
/* About */
.about{position:absolute;top:580px;left:0;width:1200px;text-align:center}
.about p{width:860px;margin:0 auto;font-size:14px;line-height:24px;color:var(--white)}
.about .lead{margin-top:60px}
.about .more{margin-top:16px}
.about .btn{margin-top:52px}
/* Rooms */
.rooms{position:absolute;top:1130px;left:0;width:1200px;height:580px;background:var(--panel);text-align:center;padding-top:46px}
.room-grid{display:flex;gap:8px;justify-content:center;margin-top:54px}
.room-card{width:304px;height:244px}
.room-a{background:linear-gradient(135deg,#7a1218,#4a070b)}
.room-b{background:linear-gradient(180deg,#2a2a2a,#0a0a0a)}
.room-c{background:linear-gradient(135deg,#6e1016,#3e0508)}
.rooms .btn{margin-top:54px}
/* Upgrade */
.upgrade{position:absolute;top:1712px;left:0;width:1200px;height:236px;text-align:center;padding-top:64px}
.upgrade-bg{position:absolute;inset:0;background:linear-gradient(90deg,#a30a12,#d4101b 50%,#a30a12)}
.upgrade h2,.upgrade p{position:relative}
.upgrade p{font-size:14px;margin-top:14px}
/* Benefits */
.benefits{position:absolute;top:2010px;left:0;width:1200px;text-align:center}
.benefits .sub{font-size:14px;margin-top:20px}
.benefit-list{display:flex;justify-content:center;gap:28px;margin-top:40px;list-style:none}
.benefit{width:160px}
.benefit-icon{width:56px;height:56px;border-radius:50%;background:var(--red);margin:0 auto;display:flex;align-items:center;justify-content:center}
.benefit-kicker{font-family:var(--head);color:var(--red);font-size:14px;margin-top:10px;text-transform:uppercase}
.benefit-name{font-weight:700;font-size:14px;line-height:19px;margin-top:4px}
.benefit-link{display:block;font-family:var(--head);color:var(--red);font-size:11px;margin-top:14px;text-transform:uppercase}
.benefit-slant{position:absolute;left:0;top:2420px}
/* Audience */
.audience{position:absolute;top:2610px;left:0;width:1200px;text-align:center}
.audience-grid{display:flex;justify-content:center;gap:24px;margin-top:58px}
.audience-card{position:relative;width:250px;height:260px;background:var(--card);border-radius:6px;padding:64px 22px 0}
.audience-icon{position:absolute;top:-34px;left:89px;width:72px;height:72px;border-radius:50%;background:var(--white);display:flex;align-items:center;justify-content:center}
.audience-card.featured .audience-icon{background:var(--red)}
.audience-card h3{font-family:var(--head);font-weight:600;font-size:16px;text-transform:uppercase}
.audience-card.featured h3{color:var(--red)}
.audience-card p{font-size:12px;line-height:18px;color:var(--grey);margin-top:10px}
.audience-card a{display:block;font-family:var(--head);font-size:12px;color:var(--grey);margin-top:14px;text-decoration:none;text-transform:uppercase}
.footer-slant{position:absolute;left:0;top:3040px}
/* Footer */
.site-footer{position:absolute;top:3170px;left:0;width:1200px;height:386px;text-align:center;background:linear-gradient(180deg,#0b0b0b,#151515)}
.footer-brand{display:inline-flex;align-items:center;gap:12px;font-family:var(--head);font-weight:600;font-size:64px;margin-top:70px;line-height:1}
.footer-brand .brand-mark{width:18px;height:18px}
.footer-links{display:flex;gap:34px;justify-content:center;list-style:none;margin-top:40px}
.footer-links a{color:var(--white);text-decoration:none;font-family:var(--head);font-size:14px}
.socials{display:flex;gap:18px;justify-content:center;margin-top:30px;list-style:none}
.socials li{width:34px;height:34px;border-radius:50%;background:var(--red)}
.copyright{font-size:12px;margin-top:30px;color:var(--grey)}
.copyright span{color:var(--red)}
</style>
</head>
<body>
<div class="page">

  <section class="hero">
    <div class="hero-bg" role="img" aria-label="Red-lit maze walls seen from above"></div>
    <svg class="hero-slant" width="1200" height="110" viewBox="0 0 1200 110" aria-hidden="true">
      <polygon points="0,110 1200,40 1200,110" fill="#0b0b0b"/>
      <polygon points="0,20 1200,0 1200,40 0,110" fill="#e3000f"/>
      <polygon points="0,0 1200,0 0,20" fill="#6a0a0e"/>
    </svg>
    <div class="hero-content">
      <div class="hero-logo"><span class="brand-mark"></span>LOCKWICK</div>
      <p class="hero-tag">ESCAPE ROOMS FOR EVERY PARTY</p>
      <div class="hero-actions">
        <a class="btn" href="#">Pine Hollow</a>
        <a class="btn btn-light" href="#">Riverton</a>
      </div>
    </div>
  </section>

  <header class="site-nav">
    <div class="brand"><span class="brand-mark"></span>LOCKWICK</div>
    <ul class="nav-links">
      <li class="active"><a href="#">HOME</a></li>
      <li><a href="#">ABOUT US</a></li>
      <li><a href="#">ESCAPE ROOMS</a></li>
      <li><a href="#">FAQ</a></li>
      <li><a href="#">GALLERY</a></li>
      <li><a href="#">GIFT CARDS</a></li>
      <li><a href="#">CONTACT</a></li>
    </ul>
  </header>

  <section class="about">
    <h2 class="section-title">About Lockwick Puzzle Hall</h2>
    <div class="title-bar"></div>
    <p class="lead">Lockwick Puzzle Hall is the heart-pounding, code-cracking, mind-bending race against time experience that Riverton and Pine Hollow have been waiting for. With five unique experiences to choose from, our escape rooms offer a sense of adventure that only children's action films can match. However, our escape rooms are not for the faint of heart.</p>
    <p class="more">We offer clean fun in a safe environment, but because we have some of the best escape rooms with tense themes, they can be seen as scary. Once you step inside the room, you are trapped, and anyone leaving the room early will disqualify your team's times from the leaderboard.</p>
    <a class="btn" href="#">Learn More</a>
  </section>

  <section class="rooms">
    <h2 class="section-title">Find The Right Room For You</h2>
    <div class="title-bar"></div>
    <div class="room-grid">
      <div class="room-card room-a" role="img" aria-label="Room artwork: a figure on a red background"></div>
      <div class="room-card room-b" role="img" aria-label="Room artwork: an island prison at night"></div>
      <div class="room-card room-c" role="img" aria-label="Room artwork: a house on a red background"></div>
    </div>
    <a class="btn" href="#">View All</a>
  </section>

  <section class="upgrade">
    <div class="upgrade-bg" role="img" aria-label="Red maze texture"></div>
    <h2 class="section-title">Upgrade To A Private Experience</h2>
    <p>Multiple parties can book the same room. If you would like to book a private experience, please contact us by phone.</p>
  </section>

  <section class="benefits">
    <h2 class="section-title">Discover The Benefits Of Escape Rooms</h2>
    <div class="title-bar"></div>
    <p class="sub">Escape rooms are fun foster teamwork and give you a sense of accomplishment.</p>
    <ul class="benefit-list">
      <li class="benefit">
        <div class="benefit-icon"><svg width="28" height="28" viewBox="0 0 28 28"><path d="M4 6h20v12H12l-6 5v-5H4z" fill="none" stroke="#fff" stroke-width="2.2"/></svg></div>
        <p class="benefit-kicker">Improve</p>
        <p class="benefit-name">Communication And Social Skills</p>
        <span class="benefit-link">Learn More</span>
      </li>
      <li class="benefit">
        <div class="benefit-icon"><svg width="28" height="28" viewBox="0 0 28 28"><circle cx="14" cy="11" r="7" fill="none" stroke="#fff" stroke-width="2.2"/><path d="M11 20h6M11 24h6" stroke="#fff" stroke-width="2.2"/></svg></div>
        <p class="benefit-kicker">Challenge Your</p>
        <p class="benefit-name">Creative Thinking And Problem Solving Skills</p>
        <span class="benefit-link">Learn More</span>
      </li>
      <li class="benefit">
        <div class="benefit-icon"><svg width="28" height="28" viewBox="0 0 28 28"><path d="M14 3l3.2 7 7.3.7-5.5 4.9 1.6 7.4L14 19.3 7.4 23l1.6-7.4L3.5 10.7l7.3-.7z" fill="none" stroke="#fff" stroke-width="2"/></svg></div>
        <p class="benefit-kicker">Enhance And</p>
        <p class="benefit-name">Build Your Memory</p>
        <span class="benefit-link">Learn More</span>
      </li>
      <li class="benefit">
        <div class="benefit-icon"><svg width="28" height="28" viewBox="0 0 28 28"><circle cx="14" cy="14" r="10" fill="none" stroke="#fff" stroke-width="2.2"/><circle cx="10.5" cy="12" r="1.4" fill="#fff"/><circle cx="17.5" cy="12" r="1.4" fill="#fff"/><path d="M9.5 16.5q4.5 4 9 0" fill="none" stroke="#fff" stroke-width="2"/></svg></div>
        <p class="benefit-kicker">Improve</p>
        <p class="benefit-name">Your Mood</p>
        <span class="benefit-link">Learn More</span>
      </li>
      <li class="benefit">
        <div class="benefit-icon"><svg width="28" height="28" viewBox="0 0 28 28"><circle cx="14" cy="14" r="10" fill="none" stroke="#fff" stroke-width="2.2"/><circle cx="14" cy="14" r="5" fill="none" stroke="#fff" stroke-width="2.2"/><circle cx="14" cy="14" r="1.6" fill="#fff"/></svg></div>
        <p class="benefit-kicker">Increase Your</p>
        <p class="benefit-name">Attention To Detail</p>
        <span class="benefit-link">Learn More</span>
      </li>
    </ul>
  </section>

  <svg class="benefit-slant" width="1200" height="130" viewBox="0 0 1200 130" aria-hidden="true">
    <polygon points="0,120 1200,20 1200,50 0,130" fill="#e3000f"/>
    <polygon points="0,130 1200,50 1200,130" fill="#0b0b0b"/>
  </svg>

  <section class="audience">
    <h2 class="section-title">Lockwick Who</h2>
    <div class="title-bar"></div>
    <div class="audience-grid">
      <article class="audience-card">
        <div class="audience-icon"><svg width="34" height="34" viewBox="0 0 34 34"><circle cx="17" cy="11" r="5" fill="#e3000f"/><circle cx="7" cy="15" r="3.5" fill="#e3000f"/><circle cx="27" cy="15" r="3.5" fill="#e3000f"/><path d="M8 30q9-16 18 0z" fill="#e3000f"/></svg></div>
        <h3>Team Building</h3>
        <p>What better way to foster synergy and teamwork than to be locked in a room together?</p>
        <a href="#">Learn More</a>
      </article>
      <article class="audience-card featured">
        <div class="audience-icon"><svg width="34" height="34" viewBox="0 0 34 34"><rect x="4" y="11" width="26" height="14" rx="7" fill="none" stroke="#fff" stroke-width="2.4"/><path d="M11 15v6M8 18h6" stroke="#fff" stroke-width="2.2"/><circle cx="23" cy="16" r="1.5" fill="#fff"/><circle cx="25" cy="20" r="1.5" fill="#fff"/></svg></div>
        <h3>Gamers</h3>
        <p>Have you been looking for a new way to impress your friends with your amazing crypto game?</p>
        <a href="#">Learn More</a>
      </article>
      <article class="audience-card">
        <div class="audience-icon"><svg width="34" height="34" viewBox="0 0 34 34"><circle cx="12" cy="11" r="4.5" fill="#e3000f"/><circle cx="23" cy="11" r="4.5" fill="#e3000f"/><path d="M3 29q9-15 18 0zM14 29q9-15 18 0z" fill="#e3000f"/></svg></div>
        <h3>Friends And Family</h3>
        <p>Bring your family, friends, neighbors, or a stranger you just met, and join us for an hour.</p>
        <a href="#">Learn More</a>
      </article>
      <article class="audience-card">
        <div class="audience-icon"><svg width="34" height="34" viewBox="0 0 34 34"><path d="M17 31s-9-10-9-17a9 9 0 0 1 18 0c0 7-9 17-9 17z" fill="none" stroke="#e3000f" stroke-width="2.6"/><circle cx="17" cy="14" r="3.5" fill="#e3000f"/></svg></div>
        <h3>Tourists And Visitors</h3>
        <p>Looking for an interactive experience for your entire group to enjoy together? You found it.</p>
        <a href="#">Learn More</a>
      </article>
    </div>
  </section>

  <svg class="footer-slant" width="1200" height="130" viewBox="0 0 1200 130" aria-hidden="true">
    <polygon points="0,0 1200,110 1200,130 0,40" fill="#e3000f"/>
    <polygon points="0,40 1200,130 0,130" fill="#0b0b0b"/>
  </svg>

  <footer class="site-footer">
    <div class="footer-brand"><span class="brand-mark"></span>LOCKWICK</div>
    <ul class="footer-links">
      <li><a href="#">HOME</a></li>
      <li><a href="#">ABOUT US</a></li>
      <li><a href="#">ESCAPE ROOMS</a></li>
      <li><a href="#">FAQ</a></li>
      <li><a href="#">GALLERY</a></li>
      <li><a href="#">GIFT CARDS</a></li>
      <li><a href="#">CONTACT</a></li>
    </ul>
    <ul class="socials" aria-label="Social links">
      <li></li><li></li><li></li><li></li>
    </ul>
    <p class="copyright">© copyrights 2022 <span>Lockwick Puzzle Hall</span> | All rights reserved</p>
  </footer>

</div>
</body>
</html>
```